Mobile Fitness snd Therapy Business Card Design

I need a business card designed for my mobile fitness and therapy business.

Please view the images that I have uploaded. I like the simplicity of the design that I have attached. I adapted it with my information

Target Market(s)

Those seeking personal training, injury rehabilitation or massage therapy.

Industry/Entity Type

Business

Contact Information for Business Card

Derek Holloway - MSc, CAT(C), RMT, CSCS, Pn2
e-mail: derek@bravuumfit.example
website: www.bravuumfit.example
instagram: @derek_holloway

Font styles to use
Sans Serif

Colors
3176b5
0355a3

Requirements
Must have
• "Contact us to receive a FREE assessment"
• Services offered:
• Personal Training
• Golf Fitness
• Injury Rehab
• Massage Therapy
• Yoga
Nice to have
• Consistent colours with brand
• - Dark Blue: #232837
• - Blue: #5096f0
• Consistent look/feel with the website: www.bravuumfit.example

```html
<!DOCTYPE html>
<html lang="en">
<head>
<meta charset="utf-8">
<title>Bravuum Business Card</title>
<link rel="stylesheet" href="https://fonts.googleapis.com/css2?family=Montserrat:wght@400;500;600;700&family=Roboto:wght@400;500;700&display=swap">
<style>
  :root {
    --navy: #232837;
    --navy-soft: #2b3145;
    --blue: #5096f0;
    --blue-light: #7fb2f3;
    --paper: #f4f4f2;
    --ink: #1f2433;
    --backdrop: #e6e7ea;
    --rule: #8a8d96;
  }
  * { box-sizing: border-box; margin: 0; padding: 0; }
  html, body { width: 1200px; height: 1000px; overflow: hidden; }
  body {
    background: var(--backdrop);
    font-family: "Montserrat", sans-serif;
    position: relative;
  }
  .card {
    position: absolute;
    width: 640px;
    height: 366px;
    border-radius: 22px;
    overflow: hidden;
    box-shadow: 0 10px 28px rgba(20, 24, 36, 0.22);
  }

  /* Front: dark side */
  .card-front {
    left: 110px;
    top: 90px;
    background: var(--navy);
    color: #fff;
  }
  .front-brand {
    position: absolute;
    left: 0; right: 0; top: 92px;
    text-align: center;
    font-weight: 600;
    font-size: 64px;
    letter-spacing: 8px;
    color: #fff;
  }
  .front-tagline {
    position: absolute;
    left: 0; right: 0; top: 172px;
    text-align: center;
    font-weight: 500;
    font-size: 17px;
    letter-spacing: 6px;
    color: #fff;
  }
  .front-services {
    position: absolute;
    left: 0; right: 0; top: 218px;
    text-align: center;
    font-family: "Roboto", sans-serif;
    font-size: 15px;
    color: var(--blue-light);
  }
  .front-cta {
    position: absolute;
    left: 50%; top: 262px;
    transform: translateX(-50%);
    white-space: nowrap;
    padding: 5px 12px;
    border: 1.5px solid #d9dbe1;
    border-radius: 4px;
    font-family: "Roboto", sans-serif;
    font-weight: 500;
    font-size: 17px;
    color: #fff;
  }
  .front-cta .highlight { color: var(--blue); font-weight: 700; }

  /* Back: white side */
  .card-back {
    left: 450px;
    top: 530px;
    background: var(--paper);
    color: var(--ink);
  }
  .back-wave { position: absolute; left: 0; bottom: 0; width: 640px; height: 366px; }
  .back-logo {
    position: absolute;
    left: 42px; top: 122px;
  }
  .back-brand {
    font-weight: 600;
    font-size: 44px;
    letter-spacing: 5px;
    color: var(--ink);
  }
  .back-tagline {
    margin-top: 2px;
    font-weight: 600;
    font-size: 12px;
    letter-spacing: 3.6px;
    color: var(--ink);
  }
  .back-divider {
    position: absolute;
    left: 352px; top: 70px;
    width: 1.5px; height: 130px;
    background: var(--rule);
  }
  .back-contact {
    position: absolute;
    left: 372px; top: 66px;
  }
  .contact-name { font-weight: 700; font-size: 19px; }
  .contact-credentials { font-size: 12.5px; margin: 2px 0 10px; }
  .contact-row {
    display: flex; align-items: center; gap: 8px;
    font-size: 14px; line-height: 22px;
  }
  .contact-icon { width: 14px; height: 14px; flex: none; }
</style>
</head>
<body>

<section class="card card-front" aria-label="Card front">
  <div class="front-brand">BRAVUUM</div>
  <div class="front-tagline">NUTRITION - FITNESS - HEALTH</div>
  <div class="front-services">Personal Training | Golf Fitness | Injury Rehab | Massage Therapy | Yoga</div>
  <div class="front-cta">Contact us to receive a <span class="highlight">FREE</span> assessment.</div>
</section>

<section class="card card-back" aria-label="Card back">
  <svg class="back-wave" viewBox="0 0 640 366" aria-hidden="true">
    <path d="M0 366 C 120 250, 300 330, 440 250 C 530 200, 600 150, 640 120 L 640 366 Z" fill="#5096f0"/>
    <path d="M0 366 C 140 275, 310 345, 450 268 C 540 220, 605 170, 640 140 L 640 366 Z" fill="#232837"/>
  </svg>

  <div class="back-logo">
    <div class="back-brand">BRAVUUM</div>
    <div class="back-tagline">NUTRITION - FITNESS - HEALTH</div>
  </div>

  <div class="back-divider"></div>

  <div class="back-contact">
    <div class="contact-name">Derek Holloway</div>
    <div class="contact-credentials">MSc, CAT(C), RMT, CSCS, Pn2</div>
    <div class="contact-row">
      <svg class="contact-icon" viewBox="0 0 14 14" aria-hidden="true"><rect x="0.5" y="0.5" width="13" height="13" rx="3" fill="#5096f0"/><path d="M3 4.5h8v5H3z M3 4.5l4 3 4-3" fill="none" stroke="#fff" stroke-width="1"/></svg>
      <span>derek@bravuumfit.example</span>
    </div>
    <div class="contact-row">
      <svg class="contact-icon" viewBox="0 0 14 14" aria-hidden="true"><rect x="0.5" y="0.5" width="13" height="13" rx="3" fill="#5096f0"/><circle cx="7" cy="7" r="3.6" fill="none" stroke="#fff" stroke-width="1"/><path d="M3.4 7h7.2M7 3.4v7.2" stroke="#fff" stroke-width="0.8"/></svg>
      <span>www.bravuumfit.example</span>
    </div>
    <div class="contact-row">
      <svg class="contact-icon" viewBox="0 0 14 14" aria-hidden="true"><circle cx="7" cy="7" r="6.5" fill="#5096f0"/></svg>
      <span>@derek_holloway</span>
    </div>
  </div>
</section>

</body>
</html>
```